Website design for Interior Designer

We want a modern website design for an Interior designer. The website should include completed and undergoing projects, CV, services, news, contact and media gallery pages.

Target Market(s)

People or companies who want to design their properties.

Industry/Entity Type

Interior

Number of Pages Required

5+ page

Requirements
Must have
• Related to interior design.
• Portrait of the designer.
• Her CV.
• Current and completed projects.
• Colours as the attached document.
• Pages mentioned in the description
Nice to have
• Like these websites – but don't copy them😊
• www.plovanstudio.co.za
• www.brightwellfixes.co.za
• www.tkstudioltd.com
• others-
• www.haraldbeuk.de/en
• www.emfairley.co.uk/
• Hope that gives you a starting point.

```html
<!DOCTYPE html>
<html lang="en">
<head>
<meta charset="utf-8">
<title>Contact | Nora Varden Interior Design</title>
<link href="https://fonts.googleapis.com/css2?family=Cabin:wght@400;600&display=swap" rel="stylesheet">
<style>
  :root {
    --room-light: #e4e6ea;
    --room-mid: #b9bec8;
    --room-wood: #b58f6a;
    --header-bg: rgba(45, 45, 48, 0.78);
    --panel-bg: rgba(22, 22, 24, 0.88);
    --field-bg: #c9c8e2;
    --field-bg-soft: #d6d5ec;
    --field-text: #4b4a2c;
    --heading-text: #d8d2c6;
    --nav-text: #f2f2f2;
    --nav-muted: #b8b8b8;
    --accent-teal: #2fe3c2;
    --accent-red: #ff0037;
    --submit-text: #f3a3b5;
    --footer-bg: rgba(40, 42, 46, 0.72);
    --footer-text: #ffffff;
    --social-one: #3fc6d2;
    --social-two: #4a6ff0;
    --logo-yellow: #ffff00;
  }
  * { margin: 0; padding: 0; box-sizing: border-box; }
  html, body { width: 1200px; height: 675px; overflow: hidden; }
  body {
    font-family: "Cabin", "Trebuchet MS", sans-serif;
    position: relative;
    background: var(--room-mid);
  }
  .hero-photo {
    position: absolute; inset: 0;
    background:
      linear-gradient(90deg, rgba(31,95,196,0.55) 0%, rgba(31,95,196,0.35) 20%, transparent 30%),
      linear-gradient(180deg, var(--room-light) 0%, var(--room-mid) 60%, var(--room-wood) 100%);
  }
  .site-header {
    position: absolute; left: 0; top: 0; width: 1200px; height: 75px;
    background: var(--header-bg);
  }
  .brand {
    position: absolute; left: 257px; top: 8px; width: 90px;
    display: flex; flex-direction: column; align-items: flex-start; gap: 5px;
    color: var(--nav-text); font-weight: 600; font-size: 16px; line-height: 19px;
    text-shadow: 0 1px 3px rgba(0,0,0,0.6);
  }
  .brand-square { width: 18px; height: 18px; background: var(--logo-yellow); }
  .main-nav a {
    position: absolute; top: 26px;
    color: var(--nav-text); text-decoration: none; font-size: 17px;
    text-shadow: 0 1px 3px rgba(0,0,0,0.6);
  }
  .main-nav .is-hover { color: var(--accent-teal); }
  .main-nav .is-muted { color: var(--nav-muted); }
  .main-nav .is-current {
    top: 12px; width: 84px; height: 50px; line-height: 50px; text-align: center;
    background: rgba(30,30,32,0.85); border-radius: 5px;
  }
  .contact-panel {
    position: absolute; left: 200px; top: 94px; width: 816px; height: 517px;
    background: var(--panel-bg); border-radius: 8px;
  }
  .contact-intro {
    position: absolute; left: 42px; top: 30px;
    color: var(--heading-text); font-size: 20px; line-height: 26px;
  }
  .field {
    position: absolute; border: none; border-radius: 7px;
    background: var(--field-bg); color: var(--field-text);
    font-family: inherit; font-size: 20px; padding: 0 9px;
  }
  .field-name { left: 41px; top: 136px; width: 311px; height: 45px; }
  .field-email { left: 41px; top: 201px; width: 311px; height: 45px; }
  .field-subject { left: 41px; top: 266px; width: 311px; height: 45px; }
  .field-message {
    left: 400px; top: 136px; width: 370px; height: 175px;
    background: var(--field-bg-soft); padding: 12px 23px; resize: none;
  }
  .field::placeholder { color: var(--field-text); }
  .submit-button {
    position: absolute; left: 41px; top: 336px; width: 729px; height: 41px;
    border: none; border-radius: 6px; background: var(--accent-red);
    color: var(--submit-text); font-family: inherit; font-size: 25px; font-weight: 600;
  }
  .site-footer {
    position: absolute; left: 0; top: 620px; width: 1200px; height: 55px;
    background: var(--footer-bg); border-top: 1px solid var(--accent-teal);
    color: var(--footer-text); font-size: 15px; font-weight: 600; line-height: 19px;
    text-shadow: 0 1px 2px rgba(0,0,0,0.6);
  }
  .footer-identity { position: absolute; left: 200px; top: 8px; }
  .footer-phones { position: absolute; left: 707px; top: 8px; }
  .footer-countries { position: absolute; left: 835px; top: 8px; }
  .social-link {
    position: absolute; top: 9px; width: 38px; height: 38px; border-radius: 50%;
  }
  .social-one { left: 915px; background: var(--social-one); }
  .social-two { left: 970px; background: var(--social-two); }
</style>
</head>
<body>
  <div class="hero-photo" role="img" aria-label="Photo of a bright meeting room with a blue sofa, framed print and long table"></div>

  <header class="site-header">
    <div class="brand"><span class="brand-square"></span><span>Nora<br>Varden</span></div>
    <nav class="main-nav">
      <a href="#" class="is-hover" style="left:373px">Home</a>
      <a href="#" class="is-muted" style="left:463px">About me</a>
      <a href="#" style="left:580px">News</a>
      <a href="#" style="left:663px">Services</a>
      <a href="#" style="left:763px">Projects</a>
      <a href="#" style="left:863px">Gallery</a>
      <a href="#" class="is-current" style="left:946px">Contact</a>
    </nav>
  </header>

  <main class="contact-panel">
    <p class="contact-intro">Do you have some questions?<br>Feel free to contact me!</p>
    <form>
      <input class="field field-name" type="text" placeholder="Name">
      <input class="field field-email" type="email" placeholder="Email address">
      <input class="field field-subject" type="text" placeholder="Subject">
      <textarea class="field field-message" placeholder="Message"></textarea>
      <button class="submit-button" type="submit">Submit</button>
    </form>
  </main>

  <footer class="site-footer">
    <div class="footer-identity">nora@nvarden.com<br>Senior Interior Designer</div>
    <div class="footer-phones">+965 52480173<br>+44 7700900461</div>
    <div class="footer-countries">| Kuwait<br>| UK</div>
    <a href="#" class="social-link social-one" aria-label="Social link one"></a>
    <a href="#" class="social-link social-two" aria-label="Social link two"></a>
  </footer>
</body>
</html>
```